" A VELMIRA é uma empresa de consultoria de Administraçao Contratual de Obras (destacadamente no segmento de infraestrutura e construçao pesada); Elaboraçao de pleitos/reivindicaçoes ("claim") para reequilíbrio econômico-financeiro de contratos de empreendimentos; Gerenciamento de Projetos; Gestao de Empreendimentos; Fiscalizaçao; Auditoria; Gestao Empresarial; Planejamento e Controle de Obras; Análise de Riscos de Empreendimentos; Orçamentos; Suporte para elaboraçao, análise e gestao de contratos. A sede da VELMIRA fica em Brasília/DF, entretanto a atuaçao ocorre em todo o Brasil conforme demanda dos clientes e localizaçao de suas obras. "

```html
<!DOCTYPE html>
<html lang="pt-BR">
<head>
<meta charset="utf-8">
<title>VELMIRA — Cartão de Visita</title>
<link href="https://fonts.googleapis.com/css2?family=Exo+2:wght@400;600;800&display=swap" rel="stylesheet">
<style>
  :root {
    --bg: #e6e8ea;
    --paper: #ffffff;
    --teal: #1a6a86;
    --teal-deep: #0f4c63;
    --teal-light: #5fb3cf;
    --ice: #d6ecf4;
    --ink-soft: #8fa4ad;
  }
  * { margin: 0; padding: 0; box-sizing: border-box; }
  html, body { width: 1200px; height: 1200px; overflow: hidden; }
  body {
    background: var(--bg);
    font-family: "Exo 2", sans-serif;
    position: relative;
  }
  .card {
    position: absolute;
    left: 150px;
    width: 900px;
    height: 510px;
    overflow: hidden;
    box-shadow: 0 6px 20px rgba(0,0,0,0.12);
  }
  /* Front */
  .card-front { top: 70px; background: var(--paper); }
  .brand {
    position: absolute;
    left: 0; right: 0; top: 170px;
    display: flex; align-items: center; justify-content: center; gap: 22px;
  }
  .brand-square {
    width: 58px; height: 58px;
    background: var(--teal);
  }
  .brand-name {
    font-weight: 800;
    font-size: 92px;
    letter-spacing: 4px;
    color: var(--teal);
    line-height: 1;
  }
  .web-strip {
    position: absolute;
    left: 0; right: 0; top: 398px;
    height: 30px;
    display: flex; align-items: center;
  }
  .web-strip .rule { height: 3px; background: var(--teal); flex: 1; }
  .web-strip .rule.short { flex: 0 0 60px; }
  .web-address {
    padding: 0 20px;
    font-size: 20px;
    font-weight: 600;
    letter-spacing: 5px;
    color: var(--teal);
  }
  .edge-band {
    position: absolute;
    left: 0; right: 0; bottom: 40px;
    height: 14px;
    background: var(--teal);
  }
  .edge-band .accent {
    position: absolute; top: 4px; height: 6px; background: var(--teal-light);
  }
  .edge-band .accent.a { left: 60px; width: 180px; }
  .edge-band .accent.b { right: 60px; width: 120px; }
  /* Back */
  .card-back {
    top: 620px;
    background: linear-gradient(135deg, var(--teal) 0%, var(--teal-deep) 100%);
    color: #fff;
  }
  .contact-list {
    position: absolute; left: 60px; top: 60px;
    list-style: none;
    display: flex; flex-direction: column; gap: 18px;
  }
  .contact-list li {
    display: flex; align-items: center; gap: 16px;
    font-size: 20px; letter-spacing: 1px;
  }
  .contact-icon {
    width: 36px; height: 36px;
    background: var(--ice);
    display: flex; align-items: center; justify-content: center;
  }
  .contact-name { font-weight: 800; font-size: 28px; letter-spacing: 2px; margin-bottom: 4px; }
  .contact-role { font-size: 18px; color: var(--ice); margin-bottom: 14px; }
  .back-brand {
    position: absolute; right: 60px; bottom: 56px;
    font-weight: 800; font-size: 64px; letter-spacing: 4px;
    color: rgba(255,255,255,0.9);
  }
  .back-lines {
    position: absolute; right: 0; top: 0; width: 14px; height: 100%;
    background: var(--teal-light);
  }
</style>
</head>
<body>
  <section class="card card-front">
    <div class="brand">
      <span class="brand-square"></span>
      <span class="brand-name">VELMIRA</span>
    </div>
    <div class="web-strip">
      <span class="rule"></span>
      <span class="web-address">www.velmira.com.br</span>
      <span class="rule short"></span>
    </div>
    <div class="edge-band"><span class="accent a"></span><span class="accent b"></span></div>
  </section>

  <section class="card card-back">
    <div class="back-lines"></div>
    <ul class="contact-list">
      <li style="flex-direction:column;align-items:flex-start;gap:0">
        <span class="contact-name">Rafael Nogueira</span>
        <span class="contact-role">Diretor</span>
      </li>
      <li>
        <span class="contact-icon">
          <svg width="20" height="20" viewBox="0 0 24 24"><path d="M6.6 10.8a15 15 0 0 0 6.6 6.6l2.2-2.2a1 1 0 0 1 1-.25 11 11 0 0 0 3.6.6 1 1 0 0 1 1 1V20a1 1 0 0 1-1 1A17 17 0 0 1 3 4a1 1 0 0 1 1-1h3.5a1 1 0 0 1 1 1c0 1.25.2 2.45.6 3.6a1 1 0 0 1-.25 1z" fill="#1a6a86"/></svg>
        </span>
        +55 61 3000-0000
      </li>
      <li>
        <span class="contact-icon">
          <svg width="20" height="20" viewBox="0 0 24 24"><rect x="3" y="5" width="18" height="14" fill="none" stroke="#1a6a86" stroke-width="2"/><path d="M3 6l9 7 9-7" fill="none" stroke="#1a6a86" stroke-width="2"/></svg>
        </span>
        contato@velmira.com.br
      </li>
      <li>
        <span class="contact-icon">
          <svg width="20" height="20" viewBox="0 0 24 24"><path d="M12 2a7 7 0 0 0-7 7c0 5 7 13 7 13s7-8 7-13a7 7 0 0 0-7-7zm0 9.5a2.5 2.5 0 1 1 0-5 2.5 2.5 0 0 1 0 5z" fill="#1a6a86"/></svg>
        </span>
        Brasília - DF
      </li>
    </ul>
    <div class="back-brand">VELMIRA</div>
  </section>
</body>
</html>
```